Kobalto Cell Phone Repair

We are a small cell phone repair store in need of a redesign to our current business card to make it a more modern, cleaner design that will catch folks' attention (perhaps with rounded edges ) - But still include most of the information listed on the current card. Would like to keep the current color scheme of black/white and green. Card will not need any personnel name included. Would like to see some designs include takes on a velorin or tekvo screen as well as more traditional cards.

Target Market(s)

broad spectrum across all cell phone users

Industry/Entity Type

Cell Phone

Contact Information for Business Card

changes to front text:
keep business Logo
business address, phone number website and email. All other info optional (add gathernest and blurvo icons on card

Rear of card:

Keep repair services, change tekvo repair to slatra repair, change quorvex os repair to data recovery (with appropriate icon or substitute)
remove products text
remove pjw and ravesh from manufacturer logos, add dunbelio.

Requirements
Must have
• business Logo
• business address, phone number website and email
• keep colors to white/black/green/gray
• gathernest and blurvo icons on card
Nice to have
• Would like to see 'traditional' business card design as well as creative design incorporating incorporating front of cell phone (eg tekvo or quorvex). Rounded edges would be nice but not necessary.

```html
<!DOCTYPE html>
<html lang="en">
<head>
<meta charset="utf-8">
<title>Kobalto Cell Phone Repair – Business Card</title>
<link rel="stylesheet" href="https://fonts.googleapis.com/css2?family=Montserrat:wght@500;700;800;900&family=Open+Sans:wght@400;600;700&display=swap">
<style>
  :root{
    --green:#6abf3c;
    --green-dark:#4e9a26;
    --black:#141414;
    --charcoal:#262626;
    --gray:#8a8a8a;
    --light:#ececec;
    --white:#ffffff;
    --stage:#e4e4e1;
  }
  *{box-sizing:border-box;margin:0;padding:0}
  html,body{width:773px;height:1200px;overflow:hidden}
  body{background:var(--stage);font-family:"Open Sans",Arial,sans-serif;position:relative}

  .card{position:absolute;left:56px;width:660px;height:380px;border-radius:20px;overflow:hidden;box-shadow:0 6px 18px rgba(0,0,0,.18)}
  .card-front{top:150px;background:var(--white)}
  .card-back{top:650px;background:var(--black);color:var(--white)}

  /* front */
  .brand{position:absolute;left:36px;top:44px;width:340px;height:120px;display:flex;align-items:center;gap:16px}
  .brand-mascot{width:96px;height:112px;flex:none;border-radius:14px;background:linear-gradient(160deg,#8fd36a,var(--green-dark))}
  .brand-text{display:flex;flex-direction:column}
  .brand-name{font-family:"Montserrat",sans-serif;font-weight:900;font-size:40px;line-height:1;color:var(--green);letter-spacing:1px}
  .brand-tag{font-family:"Montserrat",sans-serif;font-weight:700;font-size:12px;line-height:1.2;color:var(--charcoal);letter-spacing:2.5px;margin-top:8px}
  .services{position:absolute;left:40px;top:206px;list-style:none}
  .services li{font-size:14px;font-weight:600;line-height:20px;color:var(--charcoal);margin-bottom:11px;display:flex;align-items:center;gap:10px}
  .services svg{width:16px;height:16px;flex:none}

  .strip{position:absolute;left:392px;top:0;width:58px;height:380px;background:var(--black)}
  .strip-core{position:absolute;left:13px;top:0;width:32px;height:380px;background:var(--green)}
  .strip-icons{position:absolute;left:0;top:48px;width:58px;display:flex;flex-direction:column;align-items:center;gap:22px}
  .strip-icons span{width:30px;height:30px;border-radius:50%;background:var(--black);display:flex;align-items:center;justify-content:center}
  .strip-icons svg{width:15px;height:15px}

  .contact{position:absolute;left:470px;top:37px;list-style:none}
  .contact li{height:52px;display:flex;align-items:center;font-size:13px;font-weight:600;color:var(--charcoal);line-height:1.25}
  .contact .social{font-weight:700;color:var(--black)}

  /* back */
  .tiles{position:absolute;left:30px;top:34px;width:600px;display:flex;justify-content:space-between}
  .tile{width:104px;text-align:center}
  .tile-art{width:104px;height:92px;border-radius:12px;background:linear-gradient(160deg,#f4f4f4,#9a9a9a);border:3px solid var(--white)}
  .tile-label{font-family:"Montserrat",sans-serif;font-weight:700;font-size:11px;letter-spacing:1px;margin-top:10px;text-transform:uppercase}

  .makers{position:absolute;left:0;top:196px;width:660px;height:64px;background:var(--green);display:flex;align-items:center;justify-content:space-around;padding:0 30px}
  .maker{font-weight:700;font-size:19px;color:var(--white);text-transform:lowercase;display:flex;align-items:center;gap:8px}
  .maker i{width:10px;height:10px;border-radius:50%;background:var(--white);display:block}

  .note{position:absolute;left:0;top:282px;width:660px;text-align:center;font-size:12px;color:var(--light)}
  .web{position:absolute;left:0;top:318px;width:660px;text-align:center;font-family:"Montserrat",sans-serif;font-weight:800;font-size:20px;letter-spacing:1px;color:var(--green)}
</style>
</head>
<body>

<section class="card card-front">
  <div class="brand">
    <div class="brand-mascot" role="img" aria-label="Lizard mascot illustration"></div>
    <div class="brand-text">
      <div class="brand-name">KOBALTO</div>
      <div class="brand-tag">CELL PHONE REPAIR</div>
    </div>
  </div>

  <ul class="services">
    <li><svg viewBox="0 0 16 16"><path d="M2 8.5l4 4 8-9" fill="none" stroke="var(--green)" stroke-width="2.6" stroke-linecap="round" stroke-linejoin="round"/></svg>Unlocking &amp; Flashing Services</li>
    <li><svg viewBox="0 0 16 16"><path d="M2 8.5l4 4 8-9" fill="none" stroke="var(--green)" stroke-width="2.6" stroke-linecap="round" stroke-linejoin="round"/></svg>Local Phones &amp; Accessories</li>
    <li><svg viewBox="0 0 16 16"><path d="M2 8.5l4 4 8-9" fill="none" stroke="var(--green)" stroke-width="2.6" stroke-linecap="round" stroke-linejoin="round"/></svg>Water Damage Recovery</li>
    <li><svg viewBox="0 0 16 16"><path d="M2 8.5l4 4 8-9" fill="none" stroke="var(--green)" stroke-width="2.6" stroke-linecap="round" stroke-linejoin="round"/></svg>Screen Repair</li>
  </ul>

  <div class="strip">
    <div class="strip-core"></div>
    <div class="strip-icons">
      <span><svg viewBox="0 0 16 16"><path d="M4 1.5h3l1 3.5-2 1.3a8 8 0 0 0 3.7 3.7L11 8l3.5 1v3a1.5 1.5 0 0 1-1.5 1.5A11.5 11.5 0 0 1 2.5 3 1.5 1.5 0 0 1 4 1.5z" fill="var(--white)"/></svg></span>
      <span><svg viewBox="0 0 16 16"><rect x="1.5" y="3.5" width="13" height="9" rx="1" fill="none" stroke="var(--white)" stroke-width="1.6"/><path d="M2 4.5l6 4.5 6-4.5" fill="none" stroke="var(--white)" stroke-width="1.6"/></svg></span>
      <span><svg viewBox="0 0 16 16"><circle cx="8" cy="8" r="6.2" fill="none" stroke="var(--white)" stroke-width="1.5"/><path d="M1.8 8h12.4M8 1.8c-3 3.4-3 9 0 12.4M8 1.8c3 3.4 3 9 0 12.4" fill="none" stroke="var(--white)" stroke-width="1.3"/></svg></span>
      <span><svg viewBox="0 0 16 16"><path d="M8 15s5-5.2 5-9A5 5 0 0 0 3 6c0 3.8 5 9 5 9z" fill="var(--white)"/><circle cx="8" cy="6" r="1.8" fill="var(--black)"/></svg></span>
      <span><svg viewBox="0 0 16 16"><circle cx="8" cy="8" r="5" fill="var(--white)"/></svg></span>
      <span><svg viewBox="0 0 16 16"><circle cx="8" cy="8" r="5" fill="var(--white)"/></svg></span>
    </div>
  </div>

  <ul class="contact">
    <li>410-555-0178</li>
    <li>info@kobaltorepair.com</li>
    <li>www.kobaltorepair.com</li>
    <li>248 Harlow Ave<br>Linfield MD 21090</li>
    <li class="social">gathernest</li>
    <li class="social">blurvo</li>
  </ul>
</section>

<section class="card card-back">
  <div class="tiles">
    <div class="tile"><div class="tile-art" role="img" aria-label="Photo of a phone with a cracked screen"></div><div class="tile-label">Cracked Screen</div></div>
    <div class="tile"><div class="tile-art" role="img" aria-label="Photo of a phone dropped in water"></div><div class="tile-label">Water Damage</div></div>
    <div class="tile"><div class="tile-art" role="img" aria-label="Photo of a phone charging port"></div><div class="tile-label">Charging Port</div></div>
    <div class="tile"><div class="tile-art" role="img" aria-label="Photo of a tablet"></div><div class="tile-label">Slatra Repair</div></div>
    <div class="tile"><div class="tile-art" role="img" aria-label="Photo of a memory card for data recovery"></div><div class="tile-label">Data Recovery</div></div>
  </div>

  <div class="makers">
    <div class="maker"><i></i>velorin</div>
    <div class="maker"><i></i>tekvo</div>
    <div class="maker"><i></i>quorvex</div>
    <div class="maker"><i></i>dunbelio</div>
  </div>

  <p class="note">Phones, tablets, cases, chargers and accessories in stock</p>
  <p class="web">www.kobaltorepair.com</p>
</section>

</body>
</html>
```